Graphic design for the use of marketing mainly in the form of promotional die cut stickers

I’m looking for a promotional design that incorporates business logo and phone number. My business is mobile mechanical repairs to earthmoving and mining equipment. Interests would also include images of services provided like earthmoving and mining equipment either reality or cartoon. Please don’t restrict yourself to the images provided as I’m always attracted to seeing the passion of the artist show through their work.
Updates

Phone number is 0four58149263

Target Market(s)

Similar people in the same industry

Industry/Entity Type

Mining, earthmoving, mechanical, diesel fitter

Requirements
Must have
• Business logo and phone number

```html
<!DOCTYPE html>
<html lang="en">
<head>
<meta charset="utf-8">
<title>Korvan Diesel – Service Stickers</title>
<link rel="stylesheet" href="https://fonts.googleapis.com/css2?family=Russo+One&family=Oswald:wght@500;700&display=swap">
<style>
  :root{
    --backdrop:#e4e4e4;
    --sticker:#ffffff;
    --ink:#111111;
    --signal-red:#e3141b;
    --phone-yellow:#f6c21a;
    --machine-yellow:#e6b12a;
    --machine-shade:#c48f1c;
  }
  *{box-sizing:border-box;margin:0;padding:0}
  html,body{width:1200px;height:610px;overflow:hidden;background:var(--backdrop)}
  .sheet{position:relative;width:1200px;height:610px}
  .sticker{position:absolute;top:68px;width:520px;height:472px;background:var(--sticker);overflow:hidden;box-shadow:0 2px 6px rgba(0,0,0,.12)}
  .sticker--earthmoving{left:68px}
  .sticker--mining{left:612px}

  .brand{position:absolute;left:30px;top:16px;display:flex;align-items:center;gap:16px}
  .brand__mark{width:86px;height:86px;border-radius:50%;background:var(--signal-red);flex:none}
  .brand__name{font-family:"Russo One",sans-serif;color:var(--ink);line-height:1;font-weight:400}
  .brand__name-main{display:block;font-size:56px;letter-spacing:1px}
  .brand__name-sub{display:block;font-family:"Oswald",sans-serif;font-weight:500;font-size:22px;letter-spacing:4px;margin-top:4px}

  .stripes{position:absolute;inset:0;width:520px;height:472px}

  .machine-photo{position:absolute;left:150px;top:116px;width:350px;height:256px}
  .sticker--earthmoving .machine-photo{background:linear-gradient(160deg,var(--machine-yellow) 0%,var(--machine-yellow) 55%,var(--machine-shade) 100%)}
  .sticker--mining .machine-photo{background:linear-gradient(200deg,var(--machine-yellow) 0%,var(--machine-yellow) 55%,var(--machine-shade) 100%)}

  .service-band{position:absolute;left:72px;top:134px;width:52px;height:240px;background:var(--ink)}
  .service-label{position:absolute;font-family:"Oswald",sans-serif;font-weight:700;text-transform:uppercase;white-space:nowrap;transform-origin:left top;transform:rotate(-90deg)}
  .service-label--kind{color:var(--signal-red);font-size:32px;line-height:36px;left:26px;top:436px}
  .service-label--word{color:#fff;font-size:32px;line-height:52px;left:72px;top:374px;width:240px;text-align:center}

  .phone-bar{position:absolute;left:112px;right:0;top:388px;height:64px;background:var(--ink);clip-path:polygon(16px 0,100% 0,100% 100%,0 100%)}
  .phone-number{position:absolute;left:128px;top:394px;font-family:"Russo One",sans-serif;font-size:42px;color:var(--phone-yellow);letter-spacing:1px;line-height:52px}
</style>
</head>
<body>
<main class="sheet">

  <section class="sticker sticker--earthmoving">
    <svg class="stripes" viewBox="0 0 520 472" aria-hidden="true">
      <polygon points="260,120 520,70 520,86 260,136" fill="var(--signal-red)"/>
      <polygon points="400,112 520,92 520,140 420,140" fill="var(--ink)"/>
      <polygon points="128,374 300,350 300,362 128,386" fill="var(--signal-red)"/>
    </svg>
    <div class="machine-photo" role="img" aria-label="Yellow off-road mining haul truck"></div>
    <header class="brand">
      <span class="brand__mark"></span>
      <h1 class="brand__name"><span class="brand__name-main">KORVAN</span><span class="brand__name-sub">DIESEL PTY LTD</span></h1>
    </header>
    <div class="service-band"></div>
    <span class="service-label service-label--kind">Earthmoving</span>
    <span class="service-label service-label--word">Services</span>
    <div class="phone-bar"></div>
    <p class="phone-number">0four58149263</p>
  </section>

  <section class="sticker sticker--mining">
    <svg class="stripes" viewBox="0 0 520 472" aria-hidden="true">
      <polygon points="260,120 520,70 520,86 260,136" fill="var(--signal-red)"/>
      <polygon points="400,112 520,92 520,140 420,140" fill="var(--ink)"/>
      <polygon points="128,374 300,350 300,362 128,386" fill="var(--signal-red)"/>
    </svg>
    <div class="machine-photo" role="img" aria-label="Yellow tracked hydraulic excavator with bucket lowered"></div>
    <header class="brand">
      <span class="brand__mark"></span>
      <h2 class="brand__name"><span class="brand__name-main">KORVAN</span><span class="brand__name-sub">DIESEL PTY LTD</span></h2>
    </header>
    <div class="service-band"></div>
    <span class="service-label service-label--kind">Mining</span>
    <span class="service-label service-label--word">Services</span>
    <div class="phone-bar"></div>
    <p class="phone-number">0four58149263</p>
  </section>

</main>
</body>
</html>
```